3 out of 100 people will get deadly skin cancer - we need a great illustration that shows this!

We put together a prototype image that communicates lifetime skin cancer risk. (see attached). We are looking for illustrators who can take make a new/better/cooler graphic that communicates this idea. It could be as simple as a superior illustration of the graphic we have or illustrators can propose a completely different idea.What should the illustration communicate?U.S. adults have a lifetime risk of developing skin cancer of 1 in 5. But we don't want to show 1 in 5; we want to show that number in a larger group. For example, in the attached illustration we show 20 in 100 people get skin cancer (i.e., 100 beach towels/umbrellas and 20 of them are red). Research has shown that people are more likely to accurately understand numbers like this when you convey them for larger groups (i.e., 20 out of 100 rather than 1 out of 5). U.S. adults also have a lifetime risk of 2.3% of developing the deadliest form of skin cancer (melanoma). In other words, approximately 3 in 100 people will develop melanoma in their lifetime. Ideally, a single image will convey both lifetime skin cancer risk (20 in 100) and melanoma risk (3 in 100). We will award a top three as follows: 1st place = $300, 2nd place = $250, third place = $200. We will also buy any design beyond 3rd place that we like for $100. For example, we purchased 24 designs in our last contest on Artmarketly.This research is supported by funding from the Corvane Institute of Science.

Target Market(s)

The U.S. public; individuals at high risk of developing skin cancer

Industry/Entity Type

Medicine

Colors

Designer to choose colors to be used in the design.

Requirements
Must have
• an original illustration that conveys both lifetime risk of developing skin cancer (20 in 100) and melanoma (3 in 100).
Nice to have
• It can be beach towels and umbrellas, just like our prototype, or the designers can pitch an original idea. Imagery can be realistic or cartoonish (or something in between). It should be illustrations, though. Not edited photos. The image should be in color (no black and white illustrations).
Should not have
• Photos. Clip art. Free vector images.
• We are looking for original illustrations created by the designer.

```html
<!DOCTYPE html>
<html lang="en">
<head>
<meta charset="utf-8">
<title>Skin cancer risk: 20 in 100, melanoma 3 in 100</title>
<link href="https://fonts.googleapis.com/css2?family=Raleway:wght@700&display=swap" rel="stylesheet">
<style>
  :root {
    --paper: #ffffff;
    --sand: #fce3b8;
    --sky: #3cb6e8;
    --sky-light: #9fdcf4;
    --alarm: #c9192b;
    --alarm-light: #ef4250;
    --deep: #0b1a3c;
    --ink: #111111;
  }
  * { margin: 0; padding: 0; box-sizing: border-box; }
  html, body { width: 1200px; height: 741px; overflow: hidden; background: var(--paper); }
  .poster { position: relative; width: 1200px; height: 741px; font-family: "Raleway", sans-serif; }

  .legend { position: absolute; left: 0; top: 0; width: 438px; height: 741px; background: var(--paper); }
  .legend-art { position: absolute; left: 26px; width: 275px; height: 200px; border-radius: 60px 60px 12px 12px; }
  .legend-art--clear { top: 33px; background: linear-gradient(160deg, var(--sky) 0%, var(--sky-light) 100%); }
  .legend-art--melanoma { top: 262px; background: linear-gradient(170deg, var(--alarm) 0%, var(--alarm) 45%, var(--deep) 100%); }
  .legend-art--cancer { top: 498px; background: linear-gradient(170deg, var(--alarm) 0%, var(--alarm-light) 45%, var(--sky) 100%); }
  .legend-label { position: absolute; left: 190px; font-size: 30px; font-weight: 700; color: var(--ink); line-height: 1; white-space: nowrap; }
  .legend-label--clear { top: 96px; }
  .legend-label--melanoma { top: 322px; }
  .legend-label--cancer { top: 556px; }

  .beach { position: absolute; left: 438px; top: 0; width: 762px; height: 741px; background: var(--sand); }
  .crowd {
    position: absolute; left: 16px; top: 28px;
    display: grid; grid-template-columns: repeat(10, 60px); grid-auto-rows: 56px;
    column-gap: 12.5px; row-gap: 13px;
  }
  .spot { display: block; border-radius: 18px 18px 6px 6px; background: var(--sky); }
  .spot--cancer { background: var(--alarm); }
  .spot--melanoma { background: linear-gradient(180deg, var(--alarm) 0%, var(--alarm) 50%, var(--deep) 100%); }
</style>
</head>
<body>
<main class="poster">
  <section class="legend">
    <div class="legend-art legend-art--clear" role="img" aria-label="Illustration of a blue beach umbrella and striped deck chair"></div>
    <p class="legend-label legend-label--clear">no skin cancer</p>
    <div class="legend-art legend-art--melanoma" role="img" aria-label="Illustration of a red beach umbrella and dark navy deck chair"></div>
    <p class="legend-label legend-label--melanoma">melanoma</p>
    <div class="legend-art legend-art--cancer" role="img" aria-label="Illustration of a red beach umbrella and striped deck chair"></div>
    <p class="legend-label legend-label--cancer">skin cancer</p>
  </section>

  <section class="beach">
    <div class="crowd" role="img" aria-label="Beach of 100 umbrellas with deck chairs: 20 red umbrellas for skin cancer, 3 of them with dark chairs for melanoma">
      <!-- row 1 -->
      <span class="spot" aria-hidden="true"></span><span class="spot spot--cancer" aria-hidden="true"></span><span class="spot" aria-hidden="true"></span><span class="spot" aria-hidden="true"></span><span class="spot spot--melanoma" aria-hidden="true"></span><span class="spot" aria-hidden="true"></span><span class="spot" aria-hidden="true"></span><span class="spot" aria-hidden="true"></span><span class="spot" aria-hidden="true"></span><span class="spot" aria-hidden="true"></span>
      <!-- row 2 -->
      <span class="spot" aria-hidden="true"></span><span class="spot" aria-hidden="true"></span><span class="spot" aria-hidden="true"></span><span class="spot spot--cancer" aria-hidden="true"></span><span class="spot" aria-hidden="true"></span><span class="spot" aria-hidden="true"></span><span class="spot" aria-hidden="true"></span><span class="spot" aria-hidden="true"></span><span class="spot spot--cancer" aria-hidden="true"></span><span class="spot" aria-hidden="true"></span>
      <!-- row 3 -->
      <span class="spot" aria-hidden="true"></span><span class="spot" aria-hidden="true"></span><span class="spot" aria-hidden="true"></span><span class="spot" aria-hidden="true"></span><span class="spot" aria-hidden="true"></span><span class="spot" aria-hidden="true"></span><span class="spot spot--cancer" aria-hidden="true"></span><span class="spot" aria-hidden="true"></span><span class="spot" aria-hidden="true"></span><span class="spot" aria-hidden="true"></span>
      <!-- row 4 -->
      <span class="spot" aria-hidden="true"></span><span class="spot" aria-hidden="true"></span><span class="spot spot--cancer" aria-hidden="true"></span><span class="spot" aria-hidden="true"></span><span class="spot" aria-hidden="true"></span><span class="spot" aria-hidden="true"></span><span class="spot" aria-hidden="true"></span><span class="spot" aria-hidden="true"></span><span class="spot" aria-hidden="true"></span><span class="spot" aria-hidden="true"></span>
      <!-- row 5 -->
      <span class="spot spot--cancer" aria-hidden="true"></span><span class="spot spot--melanoma" aria-hidden="true"></span><span class="spot" aria-hidden="true"></span><span class="spot" aria-hidden="true"></span><span class="spot" aria-hidden="true"></span><span class="spot spot--cancer" aria-hidden="true"></span><span class="spot" aria-hidden="true"></span><span class="spot" aria-hidden="true"></span><span class="spot" aria-hidden="true"></span><span class="spot" aria-hidden="true"></span>
      <!-- row 6 -->
      <span class="spot" aria-hidden="true"></span><span class="spot" aria-hidden="true"></span><span class="spot" aria-hidden="true"></span><span class="spot spot--cancer" aria-hidden="true"></span><span class="spot" aria-hidden="true"></span><span class="spot" aria-hidden="true"></span><span class="spot" aria-hidden="true"></span><span class="spot spot--cancer" aria-hidden="true"></span><span class="spot" aria-hidden="true"></span><span class="spot" aria-hidden="true"></span>
      <!-- row 7 -->
      <span class="spot" aria-hidden="true"></span><span class="spot" aria-hidden="true"></span><span class="spot" aria-hidden="true"></span><span class="spot" aria-hidden="true"></span><span class="spot" aria-hidden="true"></span><span class="spot spot--cancer" aria-hidden="true"></span><span class="spot" aria-hidden="true"></span><span class="spot" aria-hidden="true"></span><span class="spot" aria-hidden="true"></span><span class="spot spot--cancer" aria-hidden="true"></span>
      <!-- row 8 -->
      <span class="spot spot--cancer" aria-hidden="true"></span><span class="spot" aria-hidden="true"></span><span class="spot spot--cancer" aria-hidden="true"></span><span class="spot" aria-hidden="true"></span><span class="spot" aria-hidden="true"></span><span class="spot" aria-hidden="true"></span><span class="spot" aria-hidden="true"></span><span class="spot" aria-hidden="true"></span><span class="spot" aria-hidden="true"></span><span class="spot" aria-hidden="true"></span>
      <!-- row 9 -->
      <span class="spot" aria-hidden="true"></span><span class="spot" aria-hidden="true"></span><span class="spot" aria-hidden="true"></span><span class="spot spot--cancer" aria-hidden="true"></span><span class="spot" aria-hidden="true"></span><span class="spot" aria-hidden="true"></span><span class="spot" aria-hidden="true"></span><span class="spot spot--melanoma" aria-hidden="true"></span><span class="spot" aria-hidden="true"></span><span class="spot" aria-hidden="true"></span>
      <!-- row 10 -->
      <span class="spot" aria-hidden="true"></span><span class="spot spot--cancer" aria-hidden="true"></span><span class="spot" aria-hidden="true"></span><span class="spot" aria-hidden="true"></span><span class="spot" aria-hidden="true"></span><span class="spot spot--cancer" aria-hidden="true"></span><span class="spot" aria-hidden="true"></span><span class="spot" aria-hidden="true"></span><span class="spot" aria-hidden="true"></span><span class="spot spot--cancer" aria-hidden="true"></span>
    </div>
  </section>
</main>
</body>
</html>
```